Song Cover Art. Song Tittle Turn the Lights Up

I would like a design for my songs. I'm a producer and i prouder EDM music such as Big Room House / Electro House music. Currently i have a new songs tittle name Turn the Lights Up and i need a cover art for my songs. I'm not sure what design i have in mind right now and i would like someone to create it for me. My DJ name is DJ V.
Updates
Project Deadline Extended
Reason: Hey, i will give sometimes for you guys to create the design for me. Please do google edm cover art or brondel - turn the lights up.
Target Market(s)
Electronic Dance Music Lovers
Industry/Entity Type
House
Look and feel
Each slider illustrates characteristics of the customer's brand and the style your logo design should communicate.

```html
<!DOCTYPE html>
<html lang="en">
<head>
<meta charset="utf-8">
<title>Turn the Lights Up – DJ V</title>
<link rel="stylesheet" href="https://fonts.googleapis.com/css2?family=Montserrat:wght@900&family=Open+Sans:wght@700&display=swap">
<style>
  :root {
    --sky-deep: #050608;
    --sky-mid: #1c1f24;
    --cloud: #4a4d52;
    --flare: #ffffff;
    --doodle: #f4f4f4;
    --doodle-line: #c9c9c9;
    --title-ink: #0a0a0a;
    --artist-blue: #2a9fe6;
  }
  html, body {
    margin: 0;
    padding: 0;
    width: 1200px;
    height: 1200px;
    overflow: hidden;
    background: var(--sky-deep);
  }
  .cover {
    position: relative;
    width: 1200px;
    height: 1200px;
    overflow: hidden;
  }
  .night-sky {
    position: absolute;
    inset: 0;
    background:
      radial-gradient(circle at 960px 170px, var(--flare) 0, rgba(255,255,255,0.55) 28px, rgba(255,255,255,0.08) 130px, transparent 240px),
      radial-gradient(ellipse 520px 380px at 150px 420px, var(--cloud), transparent 70%),
      radial-gradient(ellipse 600px 420px at 220px 1060px, var(--cloud), transparent 70%),
      radial-gradient(ellipse 700px 500px at 1050px 900px, #2c2f34, transparent 70%),
      linear-gradient(160deg, var(--sky-mid), var(--sky-deep) 70%);
  }
  .doodle-field {
    position: absolute;
    left: 130px;
    top: 180px;
    width: 940px;
    height: 760px;
    transform: rotate(-4deg);
  }
  .title {
    position: absolute;
    left: 0;
    right: 0;
    top: 372px;
    margin: 0;
    text-align: center;
    font-family: "Montserrat", sans-serif;
    font-weight: 900;
    font-size: 124px;
    line-height: 1;
    letter-spacing: -2px;
    text-transform: uppercase;
    color: var(--title-ink);
    transform: rotate(-4deg);
  }
  .title span { display: block; }
  .artist {
    position: absolute;
    left: 0;
    right: 0;
    top: 968px;
    margin: 0;
    text-align: center;
    font-family: "Open Sans", sans-serif;
    font-weight: 700;
    font-size: 56px;
    letter-spacing: 0.5em;
    word-spacing: -0.28em;
    padding-left: 0.5em;
    color: var(--artist-blue);
    transform: rotate(-4deg);
  }
</style>
</head>
<body>
  <main class="cover">
    <div class="night-sky" role="img" aria-label="Black and white night sky with drifting clouds, stars and a bright lens flare at upper right"></div>
    <svg class="doodle-field" viewBox="0 0 940 760" role="img" aria-label="White hand-drawn music doodle cluster of speakers, keys and swirls behind the title">
      <path fill="var(--doodle)" d="M90 90 C180 40 300 70 400 40 C500 10 620 30 720 15 C820 0 900 60 890 150 C930 250 910 350 925 450 C940 560 910 650 810 690 C700 735 580 715 470 745 C360 770 230 750 160 710 C80 670 30 600 40 500 C10 410 45 330 25 240 C15 170 40 120 90 90 Z"/>
      <path fill="none" stroke="var(--doodle-line)" stroke-width="3" d="M90 90 C180 40 300 70 400 40 C500 10 620 30 720 15 C820 0 900 60 890 150 C930 250 910 350 925 450 C940 560 910 650 810 690 C700 735 580 715 470 745 C360 770 230 750 160 710 C80 670 30 600 40 500 C10 410 45 330 25 240 C15 170 40 120 90 90 Z"/>
    </svg>
    <h1 class="title"><span>Turn the</span><span>Lights</span><span>Up</span></h1>
    <p class="artist">DJ V</p>
  </main>
</body>
</html>
```